Create Oceanfront SEO Website – Cormant Haven

I am web developer to build a high-quality, SEO-optimized website. The site is fully structured with content, layout, and purpose clearly defined, and comes with keyword-rich SEO guidance to maximize search engine visibility. Domain names and page content are provided.

Developer Role:
Build a responsive, fast-loading website in WordPress, allowing us to edit and update content in the future.
Implement SEO best practices, including meta tags, structured data, and optimized content.
Ensure smooth navigation, intuitive UX, and visually appealing design.
Establish the website to a fully functional state, after which we will handle ongoing updates and changes.
Domain and website will be hosted by hostivel under my profile.
Key Highlights:
Structured website with ready-to-use content.
SEO-focused pages for maximum visibility.
Domains and site structure already defined.
Creative freedom in design within the provided framework.

Target Market(s)

vacationers

Industry/Entity Type

vacation and travel

Coding

Coded - Design and coding required

Colors
0054AA
0677BA
7BADD7
CADEEF
E8F1F8
0094D4
00A9DD
6FCCEA
C7EBF8
E9F6FB
00AB8E
00BBA5
67D7C9
C6EFE9
E9F9F6
FFF300
FFF600
FEFA6F
FFFEC7
FFFEE8

Requirements
Must have
• see brief

```html
<!DOCTYPE html>
<html lang="en">
<head>
<meta charset="utf-8">
<title>Cormant Haven – Oceanfront Condo in Cormant Bay</title>
<link href="https://fonts.googleapis.com/css2?family=Alice&family=Poppins:wght@400;500;600&display=swap" rel="stylesheet">
<style>
:root{
  --teal:#22c7c1;
  --ink:#1e1e1e;
  --text:#444;
  --muted:#e2e2e2;
  --band:#ececec;
  --dark:#2b2b2b;
  --white:#fff;
  --serif:'Alice', Georgia, serif;
  --sans:'Poppins', Arial, sans-serif;
}
*{box-sizing:border-box;margin:0;padding:0}
html,body{width:1200px;height:4777px;overflow:hidden}
body{position:relative;background:var(--white);font-family:var(--sans);color:var(--ink)}
.abs{position:absolute}
.photo{position:absolute;overflow:hidden}
h1,h2,h3{font-family:var(--serif);font-weight:400}
.btn{display:inline-flex;align-items:center;gap:8px;height:32px;padding:0 20px;border-radius:16px;font-size:10px;font-weight:600;text-decoration:none;white-space:nowrap}
.btn svg{width:11px;height:11px}
.btn-teal{background:var(--teal);color:var(--white)}
.btn-grey{background:var(--muted);color:var(--ink)}
.btn-line{border:1.5px solid #444;color:var(--ink);background:transparent}
.btn-ghost{border:1.5px solid rgba(255,255,255,.8);color:var(--white)}
.btn-light{background:rgba(255,255,255,.25);color:var(--white)}
.btn-white{background:var(--white);color:var(--ink)}
.row{display:flex;gap:10px;flex-wrap:wrap}

/* hero */
.hero{left:0;top:0;width:1200px;height:817px;background:linear-gradient(180deg,#5f95c4 0%,#9cc3e2 28%,#2a8ea3 38%,#1c7f8c 55%,#6d6e6a 80%,#8a7a66 100%)}
.brand{left:0;width:1200px;top:16px;text-align:center;font-family:var(--serif);font-size:36px;color:var(--white)}
.topnav{left:0;width:1200px;top:78px;display:flex;justify-content:center;gap:20px;font-size:11.5px;color:var(--white);text-transform:uppercase}
.topline{left:120px;top:121px;width:960px;height:1px;background:rgba(255,255,255,.45)}
.hero-title{left:88px;top:320px;font-size:44px;line-height:46px;color:var(--white)}
.hero-sub{left:88px;top:438px;width:440px;font-size:12.5px;line-height:22px;color:var(--white)}
.hero-btns{left:88px;top:510px}

/* intro blocks */
.card-frame{border:6px solid var(--white);border-radius:30px;box-shadow:0 2px 8px rgba(0,0,0,.12)}
.sec-title{font-size:32px;line-height:38px;color:var(--ink)}
.para{font-size:12.5px;line-height:23px;color:var(--text)}

/* features band */
.band{left:0;top:1932px;width:1200px;height:633px;background:var(--band)}
.round-btn{width:40px;height:40px;border-radius:50%;display:flex;align-items:center;justify-content:center}
.feature{position:absolute;top:2124px;width:226px;height:266px;border-radius:18px;overflow:hidden}
.feature .shot{height:170px}
.feature .label{position:absolute;left:8px;right:8px;bottom:0;height:110px;background:var(--white);border-radius:16px 16px 0 0;display:flex;align-items:center;justify-content:center;text-align:center;font-family:var(--serif);font-size:14px;line-height:21px;color:var(--ink);padding:0 12px}

/* reviews */
.center{left:0;width:1200px;text-align:center}
.quote{font-family:var(--serif);font-style:italic;font-size:19px;line-height:27px;color:#333}

/* faq */
.faq-item{position:absolute;left:678px;width:429px;height:43px;border:1.5px solid #333;border-radius:22px;display:flex;align-items:center;justify-content:space-between;padding:0 24px;font-size:11px;color:var(--ink)}
.faq-item span.plus{color:var(--teal);font-size:14px;font-weight:600}

/* footer */
.footer{left:0;top:4283px;width:1200px;height:494px;background:var(--dark)}
.foot-nav{left:0;width:1200px;top:4569px;display:flex;justify-content:center;gap:31px;font-family:var(--serif);font-size:12px;color:var(--white);text-transform:uppercase}
</style>
</head>
<body>

<!-- Hero -->
<div class="abs hero" role="img" aria-label="Balcony with a wooden deck chair overlooking the ocean shoreline and beachfront towers"></div>
<div class="abs brand">Cormant Haven</div>
<nav class="abs topnav"><span>Book our condo</span><span>About Cormant Bay</span><span>Things to do</span><span>Attractions</span><span>Events &amp; Festivals</span><span>Plan your trip</span><span>Nearby destinations</span></nav>
<div class="abs topline"></div>
<h1 class="abs hero-title">Stay in Our Cormant<br>Bay Oceanfront Condo</h1>
<p class="abs hero-sub">Your perfect Cormant Bay getaway — ocean views, modern amenities, and steps from the sand.</p>
<div class="abs hero-btns row">
  <a class="btn btn-teal">Book on StayNest</a>
  <a class="btn btn-light">Book on HomeHop</a>
  <a class="btn btn-ghost">Book on LeaseLoft</a>
</div>

<!-- Welcome -->
<div class="photo card-frame" style="left:150px;top:722px;width:370px;height:536px;background:linear-gradient(180deg,#8fbce3 0%,#b7d4ec 70%,#6c6055 88%,#4a4038 100%)" role="img" aria-label="Paragliders over the fishing pier and beach"></div>
<h2 class="abs sec-title" style="left:587px;top:903px">Welcome to Your Cormant<br>Bay Vacation Home</h2>
<p class="abs para" style="left:587px;top:995px;width:455px">Welcome to your coastal retreat, perfectly situated just steps from the beach. This pet-friendly property offers stunning ocean views and the convenience of a short walk to the shoreline, making it ideal for both relaxation and adventure. Whether you're unwinding on the balcony or strolling with your pup along the sand, this getaway blends comfort with an unbeatable location.</p>
<div class="abs row" style="left:587px;top:1157px">
  <a class="btn btn-teal">Beach <svg viewBox="0 0 12 12"><path d="M1 6h9M6.5 2.5 10 6l-3.5 3.5" stroke="currentColor" stroke-width="1.5" fill="none"/></svg></a>
  <a class="btn btn-grey">Local restaurants <svg viewBox="0 0 12 12"><path d="M1 6h9M6.5 2.5 10 6l-3.5 3.5" stroke="currentColor" stroke-width="1.5" fill="none"/></svg></a>
  <a class="btn btn-line">Attractions <svg viewBox="0 0 12 12"><path d="M1 6h9M6.5 2.5 10 6l-3.5 3.5" stroke="currentColor" stroke-width="1.5" fill="none"/></svg></a>
</div>

<!-- Explore -->
<h2 class="abs sec-title" style="left:120px;top:1426px">Explore Cormant<br>Bay, Florida</h2>
<p class="abs para" style="left:120px;top:1520px;width:395px">Cormant Bay is a charming seaside town on Florida's Atlantic coast. Known for its historic fishing pier, scenic coastal highway, family-friendly beaches, and local eateries, it's a peaceful alternative to crowded tourist destinations. Visitors love strolling the pier, enjoying fresh seafood, and exploring nearby parks and nature trails.</p>
<div class="abs row" style="left:120px;top:1689px;width:400px">
  <a class="btn btn-teal">Historic fishing pier <svg viewBox="0 0 12 12"><path d="M1 6h9M6.5 2.5 10 6l-3.5 3.5" stroke="currentColor" stroke-width="1.5" fill="none"/></svg></a>
  <a class="btn btn-grey">Scenic coastal highway <svg viewBox="0 0 12 12"><path d="M1 6h9M6.5 2.5 10 6l-3.5 3.5" stroke="currentColor" stroke-width="1.5" fill="none"/></svg></a>
  <a class="btn btn-line">Parks and nature trails <svg viewBox="0 0 12 12"><path d="M1 6h9M6.5 2.5 10 6l-3.5 3.5" stroke="currentColor" stroke-width="1.5" fill="none"/></svg></a>
</div>
<div class="photo" style="left:607px;top:1373px;width:473px;height:452px;border-radius:30px;background:linear-gradient(180deg,#2f7fd6 0%,#5a9ee0 45%,#2a6aa8 55%,#245d92 100%)" role="img" aria-label="Pelican perched against blue sky and sea"></div>

<!-- Features -->
<div class="abs band"></div>
<h2 class="abs center" style="top:2024px;font-size:32px">Why Our Condo Is Perfect for Your Stay</h2>
<div class="abs round-btn" style="left:1022px;top:2025px;background:#222"><svg width="12" height="12" viewBox="0 0 12 12"><path d="M7.5 2.5 4 6l3.5 3.5" stroke="#fff" stroke-width="1.5" fill="none"/></svg></div>
<div class="abs round-btn" style="left:1068px;top:2025px;background:var(--teal)"><svg width="12" height="12" viewBox="0 0 12 12"><path d="M4.5 2.5 8 6l-3.5 3.5" stroke="#fff" stroke-width="1.5" fill="none"/></svg></div>

<div class="feature" style="left:116px"><div class="shot" role="img" aria-label="Kids riding boogie boards in ocean surf" style="background:linear-gradient(180deg,#4aa0b8,#e9eef0)"></div><div class="label">Oceanfront<br>balcony with panoramic<br>Atlantic views</div></div>
<div class="feature" style="left:356px"><div class="shot" role="img" aria-label="White dog on a leash on the sand" style="background:linear-gradient(180deg,#c89a68,#e6d2b2)"></div><div class="label">Pet-friendly<br>accommodations<br>for dogs</div></div>
<div class="feature" style="left:596px"><div class="shot" role="img" aria-label="Sunset over the fishing pier" style="background:linear-gradient(180deg,#8c93a0,#e0a060 60%,#6a5a50)"></div><div class="label">Steps from<br>Cormant Bay shoreline</div></div>
<div class="feature" style="left:836px"><div class="shot" role="img" aria-label="Modern white kitchen with appliances" style="background:linear-gradient(180deg,#bfc3c6,#eef0f1)"></div><div class="label">Fully furnished<br>kitchen and modern<br>appliances</div></div>
<div class="feature" style="left:1076px"><div class="shot" role="img" aria-label="Aerial view of beachfront homes" style="background:linear-gradient(180deg,#7fb0cf,#bca88c)"></div><div class="label">Spacious living<br>area, bedrooms and<br>bathrooms</div></div>

<div class="abs row" style="left:408px;top:2447px">
  <a class="btn btn-teal">StayNest <svg viewBox="0 0 12 12"><path d="M1 6h9M6.5 2.5 10 6l-3.5 3.5" stroke="currentColor" stroke-width="1.5" fill="none"/></svg></a>
  <a class="btn btn-white">HomeHop <svg viewBox="0 0 12 12"><path d="M1 6h9M6.5 2.5 10 6l-3.5 3.5" stroke="currentColor" stroke-width="1.5" fill="none"/></svg></a>
  <a class="btn btn-line">LeaseLoft <svg viewBox="0 0 12 12"><path d="M1 6h9M6.5 2.5 10 6l-3.5 3.5" stroke="currentColor" stroke-width="1.5" fill="none"/></svg></a>
</div>

<!-- Reviews -->
<h2 class="abs center" style="top:2650px;font-size:32px">Gurst Reviews</h2>
<div class="photo" style="left:550px;top:2730px;width:104px;height:104px;border-radius:50%;background:linear-gradient(180deg,#d8d8d8,#6a6a6a)" role="img" aria-label="Guest portrait"></div>
<svg class="abs" style="left:184px;top:2895px" width="36" height="26" viewBox="0 0 36 26"><rect width="36" height="26" rx="13" fill="#222"/><path d="M25 13H11M16 8l-5 5 5 5" stroke="#fff" stroke-width="2.4" fill="none"/></svg>
<svg class="abs" style="left:980px;top:2895px" width="36" height="26" viewBox="0 0 36 26"><rect width="36" height="26" rx="13" fill="var(--teal)"/><path d="M11 13h14M20 8l5 5-5 5" stroke="#fff" stroke-width="2.4" fill="none"/></svg>
<p class="abs center quote" style="top:2876px">"The condo was spotless, well-equipped, and had the most beautiful<br>oceanfront views. We loved sipping coffee on the balcony every morning.<br>Definitely coming back next year!"</p>
<div class="abs center" style="top:2988px;font-size:26px;letter-spacing:2px;color:#222">★★★★★</div>
<div class="abs center" style="top:3032px;font-size:11px;font-weight:600">— DANA R., STAYNEST GUEST</div>
<div class="abs" style="left:120px;top:3128px;width:960px;height:1px;background:#ddd"></div>

<!-- Gallery -->
<h2 class="abs center" style="top:3215px;font-size:32px">Our Gallery</h2>
<svg class="abs" style="left:106px;top:3495px" width="22" height="20" viewBox="0 0 22 20"><path d="M20 10H3M10 3 3 10l7 7" stroke="#222" stroke-width="1.8" fill="none"/></svg>
<svg class="abs" style="left:1071px;top:3495px" width="22" height="20" viewBox="0 0 22 20"><path d="M2 10h17M12 3l7 7-7 7" stroke="#222" stroke-width="1.8" fill="none"/></svg>
<div class="photo" style="left:168px;top:3298px;width:159px;height:362px;border-radius:14px;background:linear-gradient(90deg,#c79a63,#e0b88a 50%,#7fb8d8)" role="img" aria-label="Decorative surfboard on a wooden wall"></div>
<div class="photo" style="left:344px;top:3348px;width:158px;height:362px;border-radius:14px;background:linear-gradient(180deg,#4a4a50,#e89a40 45%,#c06a2a 70%,#2f2420)" role="img" aria-label="Sunset over the pier and water"></div>
<div class="abs" style="left:395px;top:3500px;width:56px;height:56px;border-radius:50%;background:#fff"></div>
<div class="photo" style="left:520px;top:3298px;width:159px;height:362px;border-radius:14px;background:linear-gradient(180deg,#6eaed8,#2f8aa0 18%,#c8b89c 40%,#8aa07a 75%,#b0a08a)" role="img" aria-label="Aerial view of beach houses along the coast"></div>
<div class="photo" style="left:697px;top:3348px;width:158px;height:362px;border-radius:14px;background:linear-gradient(180deg,#8cbbe2,#b8d4ec 80%,#5b5048)" role="img" aria-label="Paragliders above the pier"></div>
<div class="photo" style="left:873px;top:3298px;width:159px;height:362px;border-radius:14px;background:linear-gradient(180deg,#e6e6e4,#d4d0c8 70%,#8a6a4c)" role="img" aria-label="Bedroom with ceiling fan and bench"></div>

<!-- FAQ -->
<div class="abs footer"></div>
<div class="photo" style="left:0;top:3826px;width:612px;height:534px;border-radius:0 60px 60px 0;background:linear-gradient(180deg,#5a7a4a,#c9cdc6 35%,#3aa7d8 55%,#5cc0e6 75%,#8a7d70)" role="img" aria-label="Outdoor swimming pool with lounge chairs and palm trees"></div>
<h2 class="abs" style="left:678px;top:3925px;font-size:32px">FAQs</h2>
<div class="faq-item" style="top:3990px"><span>Is the condo pet-friendly?</span><span class="plus">+</span></div>
<div class="faq-item" style="top:4048px"><span>How far is the condo from the beach?</span><span class="plus">+</span></div>
<div class="faq-item" style="top:4106px"><span>Can I book directly on StayNest, HomeHop, or LeaseLoft?</span><span class="plus">+</span></div>
<div class="faq-item" style="top:4163px"><span>Are there family-friendly activities nearby?</span><span class="plus">+</span></div>

<!-- Footer -->
<div class="abs center" style="top:4468px;font-family:var(--serif);font-size:46px;color:var(--white)">Cormant Haven</div>
<nav class="abs foot-nav"><span>Book our condo</span><span>About Cormant Bay</span><span>Things to do</span><span>Attractions</span><span>Events &amp; Festivals</span><span>Plan your trip</span><span>Nearby destinations</span></nav>
<div class="abs center" style="top:4705px;font-size:10px;color:var(--white)">COPYRIGHT © 2025 CORMANT BAY – ALL RIGHTS RESERVED.</div>
<div class="abs round-btn" style="left:1148px;top:4683px;width:32px;height:32px;background:var(--teal)"><svg width="10" height="10" viewBox="0 0 10 10"><path d="M2 6.5 5 3.5l3 3" stroke="#fff" stroke-width="1.4" fill="none"/></svg></div>

</body>
</html>
```